Business Card Re-Design/Update

We'd like to update out business cards. I've included our current "Style guide" which has the colour scheme of the organisation in it. I've also included the branding files with logos etc in them.

I've also included a copy of one of our existing cards so that you can see how ugly/dated they look. I'd like a fresh modern corporate look.

Target Market(s)

These are for our clients, potential clients, industry contacts - like all business cards

Contact Information for Business Card

Name
Position
Company Address - Level 1, 47 Garnet Lane, Toowong Qld 4066
Direct Phone
mobile
Email
Website -www.korvalnet.com.au
Logo

Colors

Designer to choose colors to be used in the design.

Requirements
Must have
• Main Logo
• Cards will need to be editable to be able to personalize them for each new employee.
Nice to have
• The MapOUT, HandOVER, UpKEEP would be okay to have if they can be sensibly and professionally added to the look without detracting from the main imagery.
• Maybe they could go on the back of the card? will leave this to your creative discretion as to whether/where they fit.
Should not have
• Should not have decorative or script fonts

```html
<!DOCTYPE html>
<html lang="en">
<head>
<meta charset="utf-8">
<title>korvalNET business card</title>
<link href="https://fonts.googleapis.com/css2?family=Poppins:wght@400;500;600&display=swap" rel="stylesheet">
<style>
  :root {
    --bg: #2b2b2e;
    --red: #d71f27;
    --red-deep: #b32027;
    --brown: #4a3b3b;
    --ink: #2f2f31;
    --ink-soft: #4a4a4d;
    --rule: #3a3a3c;
    --paper: #ffffff;
    --paper-shade: #f1f1f1;
  }
  * { margin: 0; padding: 0; box-sizing: border-box; }
  html, body {
    width: 1200px; height: 907px; overflow: hidden;
    background: var(--bg);
    font-family: "Poppins", sans-serif;
  }
  .stage { position: relative; width: 1200px; height: 907px; }

  .card {
    position: absolute;
    width: 540px; height: 310px;
    border-radius: 22px;
    overflow: hidden;
  }

  /* Front */
  .card--front {
    left: 50px; top: 90px;
    background: linear-gradient(35deg, var(--brown) 0%, #6e3433 45%, var(--red-deep) 75%, var(--red) 100%);
    color: var(--paper);
  }
  .front-logo {
    position: absolute; left: 0; right: 0; top: 100px;
    display: flex; justify-content: center; align-items: center; gap: 14px;
  }
  .logo-mark { width: 30px; height: 30px; background: currentColor; }
  .front-logo .wordmark { font-size: 46px; font-weight: 500; letter-spacing: -0.5px; }
  .services {
    position: absolute; left: 0; right: 0; bottom: 34px;
    display: flex; justify-content: center; align-items: center; gap: 22px;
    font-size: 19px; font-weight: 500;
  }
  .service { display: flex; align-items: center; gap: 8px; }
  .service-mark { width: 12px; height: 12px; background: currentColor; }
  .divider { width: 1px; height: 16px; background: rgba(255,255,255,.45); }

  /* Back */
  .card--back {
    left: 610px; top: 500px;
    background: linear-gradient(160deg, var(--paper) 0%, var(--paper) 55%, var(--paper-shade) 100%);
    color: var(--ink);
  }
  .back-logo {
    position: absolute; right: 30px; top: 30px;
    display: flex; align-items: center; gap: 10px;
    color: var(--ink);
  }
  .back-logo .logo-mark { width: 26px; height: 26px; background: var(--red); }
  .back-logo .wordmark { font-size: 36px; font-weight: 500; letter-spacing: -0.5px; }
  .head-rule {
    position: absolute; right: 30px; top: 86px; width: 300px; height: 1px;
    background: var(--rule);
  }
  .company-details {
    position: absolute; right: 30px; top: 96px;
    list-style: none; text-align: right;
    font-size: 11.5px; line-height: 19px; color: var(--ink-soft);
  }
  .company-details li, .phones li { display: flex; align-items: center; gap: 8px; }
  .company-details li { justify-content: flex-end; }
  .icon { width: 11px; height: 11px; flex: none; fill: var(--red); }

  .person { position: absolute; left: 30px; top: 160px; }
  .person-name { font-size: 26px; font-weight: 600; color: var(--ink); line-height: 1.1; }
  .person-role { font-size: 13px; color: var(--red); margin-top: 2px; }
  .person-rule { width: 240px; height: 1px; background: var(--rule); margin: 8px 0 6px; }
  .phones { list-style: none; font-size: 11.5px; line-height: 17px; color: var(--ink-soft); }

  .edge-band {
    position: absolute; left: 0; right: 0; bottom: 0; height: 10px;
    display: flex;
  }
  .edge-band .grey { flex: 6; background: var(--ink); }
  .edge-band .red { flex: 4; background: var(--red); }
</style>
</head>
<body>
<div class="stage">

  <section class="card card--front" aria-label="Card front">
    <div class="front-logo">
      <span class="logo-mark"></span>
      <span class="wordmark">korvalNET</span>
    </div>
    <div class="services">
      <span class="service"><span class="service-mark"></span>UpKEEP</span>
      <span class="divider"></span>
      <span class="service"><span class="service-mark"></span>HandOVER</span>
      <span class="divider"></span>
      <span class="service"><span class="service-mark"></span>MapOUT</span>
    </div>
  </section>

  <section class="card card--back" aria-label="Card back">
    <div class="back-logo">
      <span class="logo-mark"></span>
      <span class="wordmark">korvalNET</span>
    </div>
    <div class="head-rule"></div>
    <ul class="company-details">
      <li>www.korvalnet.com.au
        <svg class="icon" viewBox="0 0 12 12"><circle cx="6" cy="6" r="5.5"/><path d="M1 6h10M6 .5c2 2 2 9 0 11M6 .5c-2 2-2 9 0 11" stroke="#fff" stroke-width=".8" fill="none"/></svg></li>
      <li>mlindqvist@korvalnet.com.au
        <svg class="icon" viewBox="0 0 12 12"><rect x="0" y="2" width="12" height="8"/><path d="M0 2l6 4 6-4" stroke="#fff" stroke-width=".9" fill="none"/></svg></li>
      <li>Level 1, 47 Garnet Lane, Toowong Qld 4066
        <svg class="icon" viewBox="0 0 12 12"><path d="M6 0a4 4 0 0 1 4 4c0 3-4 8-4 8S2 7 2 4a4 4 0 0 1 4-4z"/><circle cx="6" cy="4" r="1.5" fill="#fff"/></svg></li>
    </ul>

    <div class="person">
      <div class="person-name">Mara Lindqvist</div>
      <div class="person-role">Business Development Manager</div>
      <div class="person-rule"></div>
      <ul class="phones">
        <li><svg class="icon" viewBox="0 0 12 12"><rect x="3" y="0" width="6" height="12" rx="1"/><rect x="4" y="1.5" width="4" height="7" fill="#fff"/></svg>+61 (0)412 555 019</li>
        <li><svg class="icon" viewBox="0 0 12 12"><path d="M2 0l3 3-1.5 1.5a7 7 0 0 0 4 4L9 7l3 3-2 2C5 12 0 7 0 2z"/></svg>+61 (0)7 3555 0142</li>
        <li><svg class="icon" viewBox="0 0 12 12"><path d="M2 0l3 3-1.5 1.5a7 7 0 0 0 4 4L9 7l3 3-2 2C5 12 0 7 0 2z"/></svg>+61 (0)7 3555 0100</li>
        <li><svg class="icon" viewBox="0 0 12 12"><rect x="3" y="0" width="6" height="4"/><rect x="0" y="4" width="12" height="5"/><rect x="3" y="8" width="6" height="4"/></svg>+61 (0)7 3555 0199</li>
      </ul>
    </div>

    <div class="edge-band"><span class="grey"></span><span class="red"></span></div>
  </section>

</div>
</body>
</html>
```